The calm within me tour 2019

I need an improvement of my own design for a speaking tour on shame and mental health. The advertisement will be for social media. I would like someone to remove the background and do something creative and contemporary. My preference is just my head and shoulders.

Target Market(s)

Church pastors and leaders of mental health organisations

Industry/Entity Type

Mental Health

Requirements
Must have
• The same wording as original
• Delete background and replace with something that is simple but funky

```html
<!DOCTYPE html>
<html lang="en">
<head>
<meta charset="utf-8">
<title>The calm within me tour 2019</title>
<link href="https://fonts.googleapis.com/css2?family=Roboto:ital,wght@0,400;0,500;0,700;1,700;1,900&family=Roboto+Condensed:wght@400;700&display=swap" rel="stylesheet">
<style>
  :root {
    --blue: #3f7cf5;
    --blue-pale: #c9d8fb;
    --grey-text: #8a8a8a;
    --grey-dark: #5f5f5f;
    --grey-light: #e6e6e6;
    --grey-mid: #cfcfcf;
    --white: #ffffff;
    --ink: #1c1c1c;
  }
  * { margin: 0; padding: 0; box-sizing: border-box; }
  html, body { width: 800px; height: 1200px; overflow: hidden; background: var(--white); }
  .poster {
    position: relative;
    width: 800px;
    height: 1200px;
    overflow: hidden;
    background: var(--white);
    font-family: "Roboto", Arial, sans-serif;
  }
  .band { position: absolute; left: 0; width: 800px; height: 26px; background: var(--blue); z-index: 5; }
  .band--top { top: 0; }
  .band--bottom { bottom: 0; }

  .chevrons { position: absolute; left: 0; top: 26px; width: 800px; height: 620px; }

  .title {
    position: absolute;
    left: 0; top: 150px;
    width: 800px;
    font-style: italic;
    font-weight: 700;
    font-size: 84px;
    line-height: 124px;
    color: var(--grey-text);
    white-space: nowrap;
  }
  .title .line { display: block; }
  .title .line-1 { padding-left: 118px; }
  .title .line-2 { padding-left: 88px; }
  .title .accent { color: var(--blue); }

  .year-banner { position: absolute; left: 70px; top: 430px; width: 420px; height: 110px; }
  .year {
    position: absolute;
    left: 102px; top: 430px;
    font-style: italic;
    font-weight: 900;
    font-size: 92px;
    line-height: 110px;
    color: var(--white);
    letter-spacing: 2px;
  }

  .portrait {
    position: absolute;
    left: 430px; top: 450px;
    width: 370px; height: 724px;
    background: linear-gradient(180deg, #bdbdbd 0%, #6e6e6e 30%, #1e1e1e 65%, #111 100%);
    border-radius: 160px 160px 0 0;
  }

  .decor-square {
    position: absolute;
    left: 90px; top: 780px;
    width: 300px; height: 240px;
    background: var(--blue-pale);
    opacity: 0.45;
  }

  .signature { position: absolute; left: 40px; top: 1070px; display: flex; align-items: flex-start; gap: 16px; }
  .brand { display: flex; flex-direction: column; align-items: center; gap: 6px; }
  .brand-square { width: 46px; height: 46px; background: var(--blue); }
  .brand-name { font-weight: 700; font-size: 16px; color: var(--ink); }
  .speaker { padding-top: 2px; font-family: "Roboto Condensed", Arial, sans-serif; }
  .speaker-name { font-weight: 700; font-size: 34px; color: var(--ink); line-height: 38px; }
  .speaker-tour { font-weight: 400; font-size: 22px; color: var(--ink); line-height: 26px; }
  .speaker-web { font-weight: 400; font-size: 13px; color: var(--grey-dark); line-height: 20px; }
</style>
</head>
<body>
<main class="poster">
  <div class="band band--top"></div>

  <svg class="chevrons" viewBox="0 0 800 620" aria-hidden="true">
    <polygon points="0,0 430,0 620,300 430,600 0,600" fill="var(--grey-light)" opacity="0.55"/>
    <polygon points="330,120 470,120 640,380 470,640 330,640 500,380" fill="var(--grey-light)" opacity="0.9"/>
    <polygon points="250,200 380,200 540,430 380,660 250,660 410,430" fill="var(--grey-mid)" opacity="0.45"/>
  </svg>

  <h1 class="title">
    <span class="line line-1">The <span class="accent">calm</span></span>
    <span class="line line-2"><span class="accent">within</span> me tour</span>
  </h1>

  <svg class="year-banner" viewBox="0 0 420 110" aria-hidden="true">
    <polygon points="0,0 360,0 420,55 360,110 0,110 30,55" fill="var(--grey-dark)"/>
  </svg>
  <div class="year">2019</div>

  <div class="decor-square"></div>

  <div class="portrait" role="img" aria-label="Black and white photo of the speaker, head and shoulders, in a dark t-shirt"></div>

  <footer class="signature">
    <div class="brand">
      <div class="brand-square"></div>
      <span class="brand-name">dan carver</span>
    </div>
    <div class="speaker">
      <p class="speaker-name">Dan Carver -</p>
      <p class="speaker-tour">Calm within me</p>
      <p class="speaker-web">www.dancarver.co</p>
    </div>
  </footer>

  <div class="band band--bottom"></div>
</main>
</body>
</html>
```